Mediapreneur looking for Wordpress Design for 55 plus community

I own the domain brightyearsclub.net and I have another contest going on to design the logo. I'm looking to build a site for those 55 plus who are living an active lifestyle.
I want to base my site off of this site, except make it more friendly to the 55 and over community.
http://www.varnoquill.com/
In my menu, I'd like to have the following categories. About Listen Read Watch Forum Contact and the ability to add more categories in the future (possible to external sites).
Listen will be podcasts, read will be blog posts, and watch will be videos (webinars)
Updates
I uploaded some images I bought from Pixelharbor that could be used in the design. Possibly a collage.
Videos are actually going to be webinars in the future. For example, I see a real estate agent presenting a webinar about active communities, or a financial adviser giving financial advice to my community. I was trying to simplify it for my audience, some of whom may not know what a webinar is, but I'd like to go with Webinar instead of Watch. I like read and listen, though. I plan on monetizing the site via sponsorship in podcasts and a directory of active communities I'm building. I'm possibly going to ask for sponsorship for webinars and write e-books in the future. Could you display podcasts on the home page? Maybe put the most recent blog posts below the podcasts? Also, can you put a form asking them to join my newsletter somewhere in prominent position? My call to actions are to get them to subscribe to my mailing list and listen to podcasts.
Thanks.
I changed my mind on using Webinar in the menu. I asked my mom what a webinar was and she gave me a blank look. I like the idea of using Watch instead. The menu should be in this order About Listen Read Watch Forum. Please put contact details in the header menu above the menu. Call...make up a phone number. Email..contact@brightyearsclub.net. In case you missed one of my previous public updates, Listen = Podcast, Read = Blog, and Watch = Webinar/Video.
Thanks and sorry for the changes.
Target Market(s)
55 and over
Industry/Entity Type
Build
Look and feel

```html
<!DOCTYPE html>
<html lang="en">
<head>
<meta charset="utf-8">
<title>Bright Years Club</title>
<link href="https://fonts.googleapis.com/css2?family=Roboto:ital,wght@0,300;0,400;0,500;0,700;1,400&family=Source+Sans+3:wght@400;600;700&display=swap" rel="stylesheet">
<style>
:root{
  --black:#050505;
  --green:#8dc63f;
  --green-soft:#c3de88;
  --green-band:#9fcb4a;
  --charcoal:#2f2f2f;
  --paper:#efefef;
  --card:#d8d8d8;
  --ink:#222;
  --muted:#444;
  --white:#fff;
}
*{box-sizing:border-box;margin:0;padding:0}
html,body{width:1200px;height:2192px;overflow:hidden}
body{position:relative;background:var(--white);font-family:"Roboto",sans-serif;color:var(--ink)}
.abs{position:absolute}
.btn{position:absolute;background:#161616;color:var(--white);font:700 12px "Roboto",sans-serif;display:flex;align-items:center;justify-content:center;border-radius:2px}
.section-title{position:absolute;left:0;width:1200px;text-align:center;font:300 25px "Roboto",sans-serif;letter-spacing:.5px}
.title-rule{position:absolute;left:443px;width:314px;height:2px;background:#333}
.title-rule::after{content:"";position:absolute;left:30px;right:30px;top:3px;height:8px;border-radius:50%;background:radial-gradient(ellipse at top,rgba(0,0,0,.18),transparent 70%)}
.lorem{font:italic 400 9.5px/1.45 "Roboto",sans-serif;color:var(--muted)}

/* header */
.site-header{left:0;top:0;width:1200px;height:91px;background:var(--black)}
.brand{left:248px;top:22px;color:var(--green);font:700 26px/1 "Roboto",sans-serif}
.brand small{display:block;color:var(--white);font-size:14px;letter-spacing:1px;margin-top:6px}
.contact-bar{left:668px;top:0;width:282px;height:32px;background:var(--green);clip-path:polygon(22px 0,100% 0,100% 100%,0 100%)}
.contact-bar .phone{position:absolute;left:36px;top:8px;color:#111;font:400 13px "Roboto",sans-serif;display:flex;gap:8px;align-items:center}
.contact-bar .dots{position:absolute;right:6px;top:5px;display:flex;gap:5px}
.contact-bar .dots span{width:21px;height:21px;border-radius:50%;background:#e9f4d6}
.main-nav{left:592px;top:63px;display:flex;gap:13px;font:500 10.5px "Roboto",sans-serif;color:var(--white)}
.main-nav .active{color:var(--green);border-bottom:3px solid var(--green);padding-bottom:10px}

/* hero */
.hero{left:0;top:91px;width:1200px;height:396px;background:linear-gradient(100deg,#3d5a1f 0%,#7e9c45 30%,#b7c98a 48%,#e9e6dc 62%,#d8d3c4 75%,#5f7a34 100%)}
.hero-welcome{left:248px;top:160px;font:300 33px/1 "Roboto",sans-serif;color:#111}
.hero-title{left:248px;top:188px;font:700 33px/1 "Roboto",sans-serif;color:#111}
.hero-copy{left:250px;top:225px;width:296px;font:400 9.5px/1.5 "Roboto",sans-serif;color:var(--white)}

/* newsletter */
.newsletter{left:0;top:487px;width:1200px;height:46px;background:var(--black)}
.newsletter h2{position:absolute;left:248px;top:8px;color:var(--green);font:700 17px "Source Sans 3",sans-serif}
.newsletter p{position:absolute;left:250px;top:28px;color:var(--white);font:italic 400 9px "Roboto",sans-serif}
.newsletter .field{position:absolute;left:536px;top:18px;width:246px;border-bottom:1px solid #bbb;color:#aaa;font:italic 7px "Roboto",sans-serif;padding-bottom:3px}
.newsletter .subscribe{position:absolute;left:846px;top:9px;width:105px;height:27px;border:2px solid var(--white);border-radius:3px;color:var(--white);font:700 12px "Roboto",sans-serif;display:flex;align-items:center;justify-content:center}

/* about */
.about{left:0;top:533px;width:1200px;height:193px;background:var(--green-soft)}
.about-copy{left:250px;top:84px;width:700px;text-align:center;font:400 8px/1.65 "Roboto",sans-serif;color:#333}

/* help */
.help{left:0;top:726px;width:1200px;height:496px;background:var(--charcoal)}
.card{position:absolute;top:95px;width:229px;height:356px;background:var(--card)}
.card .photo{height:183px}
.card h3{position:absolute;top:185px;left:0;width:100%;height:29px;background:var(--green-band);font:600 14px/29px "Source Sans 3",sans-serif;padding-left:9px;color:#1a1a1a}
.card p{position:absolute;left:8px;right:8px;top:228px;text-align:center;font:italic 400 8.4px/13px "Roboto",sans-serif;color:var(--muted)}
.card .btn{left:58px;top:322px;width:102px;height:25px}

/* podcasts */
.podcasts{left:0;top:1222px;width:1200px;height:405px;background:var(--paper)}
.video{left:248px;top:93px;width:399px;height:264px;border:2px solid var(--green);background:linear-gradient(135deg,#8a6c43,#c8a16a 40%,#b54a3c 60%,#3b6e8c)}
.play{left:170px;top:103px;width:56px;height:56px;border:3px solid var(--white);border-radius:50%}
.play::after{content:"";position:absolute;left:20px;top:14px;border-left:18px solid var(--white);border-top:11px solid transparent;border-bottom:11px solid transparent}
.host-bar{left:665px;top:95px;width:285px;height:28px;background:var(--green-band);border:1px solid #6aa22b}
.host-bar span{position:absolute;left:8px;top:6px;font:400 13px "Roboto",sans-serif}
.host-bar svg{position:absolute;right:6px;top:6px}
.episode-title{left:665px;top:135px;font:500 13px "Roboto",sans-serif}
.episode-lead{left:665px;top:158px;width:285px;font:400 10px/1.4 "Roboto",sans-serif;color:#333}
.episode-copy{left:665px;top:190px;width:285px}
.pager{left:538px;top:383px;display:flex;gap:6px}
.pager span{width:26px;height:4px;background:var(--green-soft)}
.pager .on{background:var(--green)}

/* blog */
.blog{left:0;top:1627px;width:1200px;height:460px;background:var(--green-soft)}
.post-main{left:248px;top:92px;width:376px;height:213px;border:1px solid #7da54a;background:linear-gradient(160deg,#a9c4d8,#6f8f55 45%,#4b5a3a 70%,#8a7b66)}
.post-title{left:248px;top:318px;font:500 14px "Roboto",sans-serif}
.post-copy{left:248px;top:342px;width:370px;font-size:8.5px}
.mini{position:absolute;left:633px;width:317px;height:124px}
.mini .thumb{position:absolute;left:0;top:0;width:111px;height:123px;border:1px solid #7da54a}
.mini h4{position:absolute;left:115px;top:2px;font:500 9.5px "Roboto",sans-serif}
.mini p{position:absolute;left:115px;top:20px;width:200px;font:400 7px/1.4 "Roboto",sans-serif;color:#333}
.mini .btn{left:116px;top:99px;width:102px;height:24px}

/* footer */
.site-footer{left:0;top:2075px;width:1200px;height:117px;background:var(--black)}
.foot-nav{position:absolute;left:0;width:1200px;top:31px;display:flex;justify-content:center;gap:18px;font:500 10.5px "Roboto",sans-serif;color:var(--white);padding-left:20px}
.foot-nav .active{color:var(--green)}
.foot-rule{position:absolute;left:0;top:74px;width:1200px;height:9px;background:#d9dfe6}
.foot-circles span{position:absolute;top:56px;width:44px;height:44px;border-radius:50%;background:#dfe5ea;border:3px solid #f4f6f8}
.copyright{position:absolute;left:248px;top:99px;color:var(--white);font:400 7.5px "Roboto",sans-serif}
</style>
</head>
<body>

<header class="abs site-header">
  <div class="abs brand">Bright Years<small>CLUB</small></div>
  <div class="abs contact-bar">
    <div class="phone">
      <svg width="11" height="11" viewBox="0 0 24 24"><path fill="#111" d="M6.6 10.8a15 15 0 0 0 6.6 6.6l2.2-2.2c.3-.3.7-.4 1-.2 1.1.4 2.3.6 3.6.6.6 0 1 .4 1 1V20c0 .6-.4 1-1 1A17 17 0 0 1 3 4c0-.6.4-1 1-1h3.5c.6 0 1 .4 1 1 0 1.3.2 2.5.6 3.6.1.3 0 .7-.2 1z"/></svg>
      0800-555-014-2288
    </div>
    <div class="dots"><span></span><span></span><span></span><span></span></div>
  </div>
  <nav class="abs main-nav">
    <span class="active">HOME</span><span>ABOUT</span><span>LISTEN</span><span>READ</span><span>WEBINARS</span><span>FORUM</span><span>CONTACT US</span>
  </nav>
</header>

<section class="abs hero" role="img" aria-label="Photo of a smiling senior couple sitting outdoors in a green park"></section>
<div class="abs hero-welcome">WELCOME</div>
<h1 class="abs hero-title">BRIGHT YEARS CLUB</h1>
<p class="abs hero-copy">Lorem Ipsum is simply dummy text of the printing and typesetting industry. Lorem Ipsum has been the industry's standard dummy text ever since the 1500s, when an unknown printer took a galley of type and scrambled it to make a type Lorem Ipsum is simply dummy text of the printing and typesetting industry. Lorem Ipsum has been the industry's standard dummy text ever since the ype</p>
<div class="btn" style="left:250px;top:323px;width:101px;height:23px">Read More</div>

<section class="abs newsletter">
  <h2>SUBSCRIBE TO NEWSLETTER</h2>
  <p>Subscribe to my Mailing List and Listen to Podcasts.</p>
  <div class="field">Enter Email</div>
  <div class="subscribe">Subscribe</div>
</section>

<section class="abs about">
  <h2 class="section-title" style="top:26px">ABOUT US</h2>
  <div class="title-rule" style="top:57px"></div>
  <p class="abs about-copy">Lorem Ipsum is simply dummy text of the printing and typesetting industry. Lorem Ipsum has been the industry's standard dummy text ever since the 1500s, when an unknown printer took a galley of type and scrambled it to make a type specimen book. It has survived not only five centuries, but also the leap into electronic typesetting, remaining essentially unchanged. It was popularised in the 1960s with the release of Letraset sheets containing Lorem Ipsum is simply dummy text of the printing and typesetting industry. Lorem Ipsum has been the industry's standard dummy text ever since the 1500s, when an unknown printer took a galley of type and scrambled it to make a type specimen book. It has survived not only five centuries, but also the leap into electronic typesetting, remaining essentially unchanged. It was popularised in the 1960s with the release of Letraset sheets containing</p>
  <svg class="abs" style="left:0;top:175px" width="1200" height="18" viewBox="0 0 1200 18"><polygon points="0,18 1200,0 1200,18" fill="var(--green-band)"/></svg>
</section>

<section class="abs help">
  <h2 class="section-title" style="top:32px;color:var(--white)">HOW WE HELP YOU ?</h2>
  <div class="title-rule" style="top:62px;background:#ddd"></div>
  <article class="card" style="left:248px">
    <div class="photo" role="img" aria-label="Senior couple reading papers at a laptop" style="background:linear-gradient(135deg,#f2efe9,#d9b7a3 55%,#c8c2b5)"></div>
    <h3>Our Podcasts</h3>
    <p>Lorem Ipsum is simply dummy text of the printing and typesetting industry. Lorem Ipsum has been the industry's standard dummy text ever since the 1500s, when an unknown printer took a galley of type and scrambled it to make a type specimen book. It has survived not only five centuries, but also the leap</p>
    <div class="btn">Read More</div>
  </article>
  <article class="card" style="left:485px">
    <div class="photo" role="img" aria-label="Smiling senior couple embracing under a blue sky" style="background:linear-gradient(160deg,#5d9bd6,#a9cdef 45%,#e8e4de)"></div>
    <h3>55 Plus Training</h3>
    <p>Lorem Ipsum is simply dummy text of the printing and typesetting industry. Lorem Ipsum has been the industry's standard dummy text ever since the 1500s, when an unknown printer took a galley of type and scrambled it to make a type specimen book. It has survived not only five centuries, but also the leap</p>
    <div class="btn">Read More</div>
  </article>
  <article class="card" style="left:722px">
    <div class="photo" role="img" aria-label="Colourful hot air balloons rising into a blue sky" style="background:linear-gradient(150deg,#9cc2e4,#5f90c4 50%,#8f3b3b 80%,#c7493a)"></div>
    <h3>Our Communities</h3>
    <p>Lorem Ipsum is simply dummy text of the printing and typesetting industry. Lorem Ipsum has been the industry's standard dummy text ever since the 1500s, when an unknown printer took a galley of type and scrambled it to make a type specimen book. It has survived not only five centuries, but also the leap</p>
    <div class="btn">Read More</div>
  </article>
</section>

<section class="abs podcasts">
  <svg class="abs" style="left:0;top:-6px" width="1200" height="14" viewBox="0 0 1200 14"><polygon points="0,6 1200,0 1200,14 0,14" fill="var(--paper)"/></svg>
  <h2 class="section-title" style="top:30px">PODCASTS</h2>
  <div class="title-rule" style="top:60px"></div>
  <div class="abs video" role="img" aria-label="Video still of seniors exercising with raised arms in a gym class">
    <div class="abs play"></div>
  </div>
  <div class="abs host-bar">
    <span>Dana Whitfield</span>
    <svg width="70" height="14" viewBox="0 0 70 14" fill="none" stroke="#111" stroke-width="1.6">
      <circle cx="7" cy="7" r="5.5"/><path d="M7 4v3l2 1.5"/>
      <circle cx="22" cy="7" r="1.6" fill="#111"/><circle cx="29" cy="3" r="1.6" fill="#111"/><circle cx="29" cy="11" r="1.6" fill="#111"/><path d="M22 7l7-4M22 7l7 4"/>
      <path d="M46 1v8M42 6l4 4 4-4M41 13h10"/>
      <circle cx="63" cy="7" r="5.5"/><path d="M61.5 4.5v5l4-2.5z" fill="#111"/>
    </svg>
  </div>
  <h3 class="abs episode-title">Marcus Ellery chats with</h3>
  <p class="abs episode-lead">Lorem Ipsum is simply dummy text of the printing psum has been the industry's standard dummy text ever since the 1500s</p>
  <p class="abs episode-copy lorem">Lorem Ipsum is simply dummy text of the printing and typesetting industry. Lorem Ipsum has been the industry's standard dummy text ever since the 1500s, when an unknown printer took a galley of type and scrambled it to make a type specimen book. It has survived not only five centuries Lorem Ipsum is simply dummy text of the printing and typesetting industry. Lorem Ipsum has been the industry's standard dummy text ever since the 1500s, when an unknown printer took a galley of type and scrambled it to make a type specimen book. It has survived not only five centuries</p>
  <div class="btn" style="left:666px;top:329px;width:102px;height:23px">Read More</div>
  <div class="abs pager"><span></span><span class="on"></span><span></span><span></span></div>
  <svg class="abs" style="left:0;top:389px" width="1200" height="16" viewBox="0 0 1200 16"><polygon points="0,16 1200,0 1200,16" fill="#c9c9c9"/></svg>
</section>

<section class="abs blog">
  <h2 class="section-title" style="top:30px">OUR BOLG</h2>
  <div class="title-rule" style="top:60px"></div>
  <div class="abs post-main" role="img" aria-label="Senior hikers resting on a mountain trail"></div>
  <h3 class="abs post-title">Lorem Ipsum is simply dummy text</h3>
  <p class="abs post-copy lorem">Lorem Ipsum is simply dummy text of the printing and typesetting industry. Lorem Ipsum has been the industry's standard dummy text ever since the 1500s, when an unknown printer took a galley of type and scrambled it to make a type specimen book. It has survived not only five centuries, but also the leap into electronic typesetting, remaining essentially unchanged.</p>
  <div class="btn" style="left:249px;top:403px;width:102px;height:24px">Read More</div>

  <article class="mini" style="top:92px">
    <div class="thumb" role="img" aria-label="Senior women laughing over a board game" style="background:linear-gradient(140deg,#e9e2d6,#d7a541 55%,#6f8fb0)"></div>
    <h4>Lorem Ipsum is simply dummy</h4>
    <p>Lorem Ipsum is simply dummy text of the printing and typesetting industry. Lorem Ipsum has been the industry's standard dummy text ever since the 1500s, when an unknown printer took a galley of type and scrambled it to make a type specimen book. It has survived not only five centuries, but also the leap into</p>
    <div class="btn">Read More</div>
  </article>
  <article class="mini" style="top:232px">
    <div class="thumb" role="img" aria-label="Smiling grandmother with her family" style="background:linear-gradient(150deg,#d8c7b0,#c98b5a 45%,#4d7fb7)"></div>
    <h4>Lorem Ipsum is simply dummy</h4>
    <p>Lorem Ipsum is simply dummy text of the printing and typesetting industry. Lorem Ipsum has been the industry's standard dummy text ever since the 1500s, when an unknown printer took a galley of type and scrambled it to make a type specimen book. It has survived not only five centuries, but also the leap into</p>
    <div class="btn">Read More</div>
  </article>
</section>

<footer class="abs site-footer">
  <svg class="abs" style="left:0;top:-12px" width="1200" height="14" viewBox="0 0 1200 14"><polygon points="0,0 1200,6 1200,14 0,14" fill="var(--green-band)"/><polygon points="0,6 1200,10 1200,14 0,14" fill="var(--black)"/></svg>
  <nav class="foot-nav">
    <span class="active">HOME</span><span>ABOUT</span><span>PODCAST</span><span>BLOG</span><span>RESOURCES</span><span>PRODUCTS</span><span>PODCAST ARCHIVES</span><span>CONTACT</span>
  </nav>
  <div class="foot-rule"></div>
  <div class="foot-circles">
    <span style="left:491px"></span><span style="left:550px"></span><span style="left:608px"></span><span style="left:664px"></span>
  </div>
  <p class="copyright">© Copyright 2016 brightyearsclub</p>
</footer>

</body>
</html>
```